Business Card Design - Koru Lantern

We (Koru Lantern) need a business card design for our boutique mobile marketing agency based in Sydney, Australia.
We work with brands and advertisers to deliver and implement end to end mobile (smartphone and tablet) marketing solutions.

We already have a logo and website design, these files will be provided. Our colours centre around a blue/orange mix (the logo containing the orange (colour code: RGB 255,165,0).

Our name and logo communicate strength and confidence. We see ourselves as being trustworthy advisors who are also fun and passionate.

Target Market(s)

Senior Marketing Managers

Industry/Entity Type

Marketing

Requirements
Must have
• Employee Name: Mark Ellery
Mobile Number: 0491 573 862
Email Address xxxx@korulantern.example
Website: www.korulantern.example
Twitter ID: KoruLantern

```html
<!DOCTYPE html>
<html lang="en">
<head>
<meta charset="utf-8">
<title>Koru Lantern – Business Card</title>
<link href="https://fonts.googleapis.com/css2?family=Open+Sans:wght@400;600;700&display=swap" rel="stylesheet">
<style>
  :root {
    --stage: #000000;
    --card: #ffffff;
    --card-edge: #9a9a9a;
    --ink-dark: #2f2f2f;
    --ink-soft: #8a8a8a;
    --orange: #f7931e;
    --mark-grey: #c4c4c4;
  }
  * { margin: 0; padding: 0; box-sizing: border-box; }
  html, body {
    width: 1200px; height: 960px; overflow: hidden;
    background: var(--stage);
    font-family: "Open Sans", Arial, sans-serif;
  }
  .canvas { position: relative; width: 1200px; height: 960px; }
  .card {
    position: absolute; top: 378px;
    width: 503px; height: 280px;
    background: var(--card);
    border: 1px solid var(--card-edge);
    overflow: hidden;
  }
  .card--front { left: 107px; border-top-left-radius: 26px; }
  .card--back { left: 624px; border-top-right-radius: 26px; }

  .brand {
    position: absolute; left: 0; right: 0; top: 118px;
    display: flex; align-items: center; justify-content: center; gap: 12px;
  }
  .brand__dot {
    width: 26px; height: 26px; border-radius: 50%;
    background: var(--orange);
  }
  .brand__name {
    font-size: 31px; font-weight: 600; color: var(--ink-dark);
    letter-spacing: 0.5px;
  }

  .brand-mark-decoration {
    position: absolute; left: 0; top: 0;
    width: 340px; height: 280px;
  }

  .contact { position: absolute; left: 196px; top: 144px; }
  .contact__name {
    font-size: 20px; font-weight: 700; color: var(--ink-dark);
    line-height: 28px; margin-bottom: 2px;
  }
  .contact__row {
    display: flex; font-size: 13px; color: var(--ink-soft);
    line-height: 21px; white-space: nowrap;
  }
  .contact__label { width: 109px; }
  .contact__sep { width: 12px; }
</style>
</head>
<body>
<div class="canvas">
  <section class="card card--front">
    <div class="brand">
      <span class="brand__dot"></span>
      <span class="brand__name">Koru Lantern</span>
    </div>
  </section>

  <section class="card card--back">
    <svg class="brand-mark-decoration" viewBox="0 0 340 280" role="img" aria-label="Large faint grey brand mark decoration">
      <defs>
        <radialGradient id="markFade" cx="0.4" cy="0.4" r="0.5">
          <stop offset="0" stop-color="#c4c4c4" stop-opacity="0.6"/>
          <stop offset="0.6" stop-color="#c4c4c4" stop-opacity="0.3"/>
          <stop offset="1" stop-color="#c4c4c4" stop-opacity="0"/>
        </radialGradient>
      </defs>
      <rect x="0" y="0" width="340" height="280" fill="url(#markFade)"/>
    </svg>

    <div class="contact">
      <h1 class="contact__name">Mark Ellery</h1>
      <div class="contact__row"><span class="contact__label">Mobile Number</span><span class="contact__sep">:</span><span>0491 573 862</span></div>
      <div class="contact__row"><span class="contact__label">Email Address</span><span class="contact__sep">:</span><span>xxxx@korulantern.example</span></div>
      <div class="contact__row"><span class="contact__label">Website</span><span class="contact__sep">:</span><span>www.korulantern.example</span></div>
      <div class="contact__row"><span class="contact__label">Twitter ID</span><span class="contact__sep">:</span><span>KoruLantern</span></div>
    </div>
  </section>
</div>
</body>
</html>
```